Tillard Environmental Projects New Website Design

I need a new website for a Environmental Project Company based in Sydney Australia, working throughout South East Asia.I've attached the company logo, please try & incorporate these colours or use complimentary colours. I've attached a word doc with design brief.I'm going to use Wix, so please ensure files are suitable.Thankyou.

Number of Pages Required

5+ page

Colors

Designer to choose colors to be used in the design.

Requirements
Must have
• Refer to Word Document
Nice to have
• Refer to Word Document
Should not have
• Not to be dark

```html
<!DOCTYPE html>
<html lang="en">
<head>
<meta charset="utf-8">
<title>Tillard Environmental Projects</title>
<link rel="stylesheet" href="https://fonts.googleapis.com/css2?family=Open+Sans:wght@400;600;700;800&display=swap">
<style>
:root{
  --teal:#13b092;
  --olive:#435a22;
  --olive-text:#4d5f1e;
  --ink:#2b2b2b;
  --body:#333;
  --muted:#777;
  --light-bg:#f3f3f3;
  --footer:#1c2219;
  --white:#fff;
  --line:#9aa0a0;
}
*{box-sizing:border-box;margin:0;padding:0}
html,body{width:1200px;height:3630px;overflow:hidden;background:var(--white)}
body{font-family:"Open Sans",Arial,sans-serif;color:var(--body);position:relative}
.abs{position:absolute}

/* header */
.site-header{position:absolute;left:0;top:0;width:1200px;height:111px;background:var(--white)}
.brand{position:absolute;left:58px;top:22px;display:flex;align-items:center;gap:14px}
.brand-dot{width:64px;height:64px;border-radius:50%;background:var(--olive)}
.brand-name{font-weight:700;font-size:17px;line-height:20px;color:var(--olive);letter-spacing:1px;text-transform:uppercase}
.main-nav{position:absolute;left:443px;top:44px;display:flex;gap:0}
.main-nav a{font-size:17px;color:var(--ink);text-decoration:none;padding:0 19px;position:relative}
.main-nav a.active{font-weight:600}
.main-nav a.active::after{content:"";position:absolute;left:2px;right:2px;bottom:-10px;height:4px;background:var(--teal)}
.main-nav a.contact{color:var(--teal)}

/* hero */
.hero{position:absolute;left:0;top:111px;width:1200px;height:630px;
  background:radial-gradient(ellipse at 50% 20%,#4c6a3a 0%,#2c3f22 45%,#111a10 100%)}
.hero-kicker{position:absolute;top:100px;width:100%;text-align:center;color:var(--teal);font-weight:700;font-size:35px}
.hero-rule{position:absolute;top:167px;left:525px;width:150px;height:2px;background:var(--white)}
.hero-title{position:absolute;top:205px;width:100%;text-align:center;color:var(--white);font-weight:700;font-size:44px;line-height:57px}
.hero-sub{position:absolute;top:335px;width:100%;text-align:center;color:#e8e8e8;font-size:25px;line-height:32px}
.btn{position:absolute;display:flex;align-items:center;justify-content:center;font-weight:700;font-size:25px;letter-spacing:1px;color:var(--white)}
.btn-solid{background:var(--teal)}
.btn-outline{border:3px solid var(--white)}
.hero-arrow{position:absolute;top:289px;width:54px;height:54px;border:2px solid var(--white);border-radius:50%}

/* headings */
.section-title{position:absolute;width:100%;text-align:center;font-weight:700;font-size:24px;color:var(--ink)}
.section-title .accent{color:var(--teal)}
.section-rule{position:absolute;left:469px;width:262px;height:2px;background:var(--teal)}

.about-text{position:absolute;left:136px;width:933px;text-align:center;font-size:14.5px;line-height:21px;color:var(--body)}

/* band */
.team-band{position:absolute;left:0;top:1148px;width:1200px;height:227px;background:var(--olive)}
.team-band p{position:absolute;left:120px;top:44px;width:960px;text-align:center;color:var(--white);font-size:13px;font-weight:600;line-height:17px}

/* services */
.services-photo{position:absolute;left:0;top:1375px;width:600px;height:632px;
  background:radial-gradient(circle at 40% 25%,#e9f1c8 0%,#a9c764 30%,#5f8a26 65%,#2f4a14 100%)}
.service-list{position:absolute;left:193px;top:1543px;width:407px;list-style:none}
.service-list li{height:41px;background:var(--white);border-bottom:3px solid var(--olive);text-align:right;padding-right:48px;line-height:38px;font-size:17px;font-weight:700;color:var(--olive-text)}
.service-list li.current{background:var(--teal);color:var(--white)}
.service-title{position:absolute;left:654px;top:1436px;font-weight:700;font-size:24px;color:var(--ink)}
.service-text{font-size:13px;line-height:19px;color:var(--body)}

/* news */
.news{position:absolute;left:0;top:2007px;width:1200px;height:635px;background:var(--light-bg)}
.news-card{position:absolute;top:109px;width:302px;height:494px;background:var(--white);border-radius:14px;overflow:hidden;box-shadow:0 2px 8px rgba(0,0,0,.2)}
.news-photo{height:267px}
.news-tag{position:absolute;left:26px;top:296px;color:var(--teal);font-weight:700;font-size:15px}
.news-title{position:absolute;left:26px;top:332px;color:#111;font-weight:700;font-size:16px}
.news-excerpt{position:absolute;left:26px;top:364px;width:255px;color:var(--muted);font-size:15px;line-height:20px}
.news-meta{position:absolute;left:26px;right:22px;top:450px;border-top:1px solid #ddd;padding-top:16px;display:flex;justify-content:space-between;font-size:11px;color:var(--body)}

/* contact */
.field{position:absolute;border:1.5px solid #8a8f8c;font-size:10px;color:#555;padding:20px 18px;text-transform:uppercase}

/* footer */
.site-footer{position:absolute;left:0;top:3271px;width:1200px;height:359px;background:var(--footer);color:var(--white)}
.footer-dot{position:absolute;left:49px;top:40px;width:104px;height:104px;border-radius:50%;border:3px solid #c9c9c9}
.footer-name{position:absolute;left:173px;top:52px;font-size:24px;line-height:28px;letter-spacing:3px;color:#d4d4d4;text-transform:uppercase}
.footer-heading{position:absolute;top:53px;font-weight:700;font-size:16px}
.footer-links{position:absolute;top:88px;list-style:none;font-size:13px;line-height:15px;text-transform:uppercase}
.social{position:absolute;top:3513px}
.gallery{position:absolute;left:874px;top:89px;display:grid;grid-template-columns:repeat(3,84px);gap:7px}
.gallery div{height:84px;border:2px solid #c9c9c9}
</style>
</head>
<body>

<header class="site-header">
  <div class="brand"><div class="brand-dot"></div><div class="brand-name">Tillard<br>Environmental<br>Projects</div></div>
  <nav class="main-nav">
    <a class="active">Home</a><a>Who we are</a><a>Services</a><a>Products</a><a>News</a><a>Blog</a><a class="contact">Contact</a>
  </nav>
</header>

<section class="hero" role="img" aria-label="Photograph of a green forest with tall trees">
  <div class="hero-kicker">TILLARD ENVIRONMENTAL PROJECTS</div>
  <div class="hero-rule"></div>
  <h1 class="hero-title">LOREM IPSUM DOLOR SIT AMET,<br>CONSECTETUER ADIPISCING</h1>
  <p class="hero-sub">Lorem ipsum dolor sit amet, consectetuer adipiscing<br>elit, sed diam nonummy nibh euismod tincidunt ut</p>
  <div class="btn btn-solid" style="left:385px;top:427px;width:208px;height:52px">WHO WE ARE</div>
  <div class="btn btn-outline" style="left:612px;top:427px;width:203px;height:52px">PRODUCTS</div>
  <div class="hero-arrow" style="left:40px"><svg width="50" height="50"><path d="M28 17 L20 25 L28 33" fill="none" stroke="#fff" stroke-width="2.5"/></svg></div>
  <div class="hero-arrow" style="left:1106px"><svg width="50" height="50"><path d="M22 17 L30 25 L22 33" fill="none" stroke="#fff" stroke-width="2.5"/></svg></div>
</section>

<section class="about">
  <h2 class="section-title" style="top:790px"><span class="accent">WHO</span> WE ARE</h2>
  <div class="section-rule" style="top:839px"></div>
  <p class="about-text" style="top:862px">Lorem ipsum dolor sit amet, consectetuer adipiscing elit, sed diam nonummy nibh euismod tincidunt ut laoreet dolore magna aliquam erat volutpat. Ut wisi enim ad minim veniam, quis nostrud exerci tation ullamcorper suscipit lobortis nisl ut aliquip ex ea commodo consequat. Duis autem vel eum iriure dolor in hendrerit in vulputate velit esse molestie consequat, vel illum dolore eu feugiat nulla facilisis at vero eros et accumsan et iusto odio dignissim qui blandit praesent luptatum zzril delenit augue duis dolore te feugait nulla facilisi.</p>
  <p class="about-text" style="top:986px">Lorem ipsum dolor sit amet, consectetuer adipiscing elit, sed diam nonummy nibh euismod tincidunt ut laoreet dolore magna aliquam erat volutpat. Ut wisi enim ad minim veniam, quis nostrud exerci tation ullamcorper suscipit lobortis nisl ut aliquip ex ea commodo consequat. Duis autem vel eum iriure dolor in hendrerit in vulputate velit esse molestie consequat, vel illum dolore eu feugiat nulla facilisis at vero eros et accumsan et iusto odio dignissim qui blandit praesent luptatum zzril delenit augue duis dolore te feugait nulla facilisi.</p>
</section>

<section class="team-band">
  <p>Lorem ipsum dolor sit amet, consectetuer adipiscing elit, sed diam nonummy nibh euismod tincidunt ut laoreet dolore magna aliquam erat volutpat. Ut wisi enim ad minim veniam, quis nostrud exerci tation ullamcorper suscipit lobortis nisl ut aliquip ex ea commodo consequat. Duis autem vel eum iriure dolor in hendrerit in vulputate velit esse molestie consequat, vel illum dolore eu</p>
  <div class="btn btn-outline" style="left:459px;top:126px;width:282px;height:57px;font-size:24px">MEET OUR TEAM</div>
</section>

<section class="services">
  <div class="services-photo" role="img" aria-label="Photograph of a glass globe resting in sunlit green grass"></div>
  <ul class="service-list">
    <li>Sustainable Food.</li>
    <li class="current">Green walls</li>
    <li>Eco gardens</li>
    <li>Living food walls</li>
    <li>Aquaculture – Fish Farm – Barramundi</li>
    <li>Hydroponic gardens.</li>
    <li>Syndicated farms.</li>
  </ul>
  <h2 class="service-title">GREEN WALLS</h2>
  <div class="abs" style="left:654px;top:1483px;width:203px;height:2px;background:var(--teal)"></div>
  <svg class="abs" style="left:654px;top:1518px" width="92" height="57" viewBox="0 0 92 57">
    <g fill="#13b092">
      <rect x="0" y="0" width="28" height="16"/><rect x="32" y="0" width="28" height="16"/><rect x="64" y="0" width="28" height="16"/>
      <rect x="0" y="20" width="12" height="16"/><rect x="16" y="20" width="28" height="16"/><rect x="48" y="20" width="28" height="16"/><rect x="80" y="20" width="12" height="16"/>
      <rect x="0" y="40" width="28" height="16"/><rect x="32" y="40" width="28" height="16"/><rect x="64" y="40" width="28" height="16"/>
    </g>
  </svg>
  <p class="service-text abs" style="left:773px;top:1516px;width:356px">Lorem ipsum dolor sit amet, consectetuer adipiscing elit, sed diam nonummy nibh euismod tincidunt ut laoreet dolore magna aliquam erat volutpat. Ut wisi enim ad minim veniam, quis nostrud exerci tation ullamcorper suscipit lobortis nisl ut aliquip ex ea</p>
  <div class="abs" style="left:654px;top:1641px;width:474px;height:2px;background:var(--teal)"></div>
  <p class="service-text abs" style="left:654px;top:1665px;width:474px">Lorem ipsum dolor sit amet, consectetuer adipiscing elit, sed diam nonummy nibh euismod tincidunt ut laoreet dolore magna aliquam erat volutpat. Ut wisi enim ad minim veniam, quis nostrud exerci tation ullamcorper suscipit lobortis nisl ut aliquip ex ea commodo consequat. Duis autem vel eum iriure dolor in hendrerit in vulputate velit esse molestie consequat, vel illum dolore eu feugiat nulla facilisis at vero eros et accumsan et iusto odio dignissim qui blandit praesent luptatum zzril delenit augue duis dolore te feugait nulla facilisi.</p>
  <div class="btn btn-solid" style="left:654px;top:1881px;width:114px;height:42px;font-size:18px">MORE</div>
</section>

<section class="news">
  <h2 class="section-title" style="top:28px">LASTEST NEWS</h2>
  <div class="section-rule" style="top:72px;background:var(--ink)"></div>
  <article class="news-card" style="left:86px">
    <div class="news-photo" role="img" aria-label="Photograph of hands holding a small green globe" style="background:radial-gradient(circle at 50% 55%,#9cd36a,#5c9a2e 55%,#3d6b1c)"></div>
    <div class="news-tag">Lorem ipsum</div><div class="news-title">LOREM NEWS TITLE</div>
    <p class="news-excerpt">Lorem ipsum doper ditun. Vid ners placerat felic celerati pitor eratin ac tupars.</p>
    <div class="news-meta"><span>By Reid Calloway</span><span>16 hours Ago</span></div>
  </article>
  <article class="news-card" style="left:449px">
    <div class="news-photo" role="img" aria-label="Photograph of wind turbines on a green field" style="background:linear-gradient(#e7ece6 0%,#d5dfd2 55%,#7aa052 70%,#4f7a2c 100%)"></div>
    <div class="news-tag">Lorem ipsum</div><div class="news-title">LOREM NEWS TITLE</div>
    <p class="news-excerpt">Lorem ipsum doper ditun. Vid ners placerat felic celerati pitor eratin ac tupars.</p>
    <div class="news-meta"><span>By Reid Calloway</span><span>16 hours Ago</span></div>
  </article>
  <article class="news-card" style="left:812px">
    <div class="news-photo" role="img" aria-label="Photograph of a young researcher holding a water sample beside a river" style="background:linear-gradient(120deg,#7f9c5c,#b7c0a8 50%,#5d7140)"></div>
    <div class="news-tag">Lorem ipsum</div><div class="news-title">LOREM NEWS TITLE</div>
    <p class="news-excerpt">Lorem ipsum doper ditun. Vid ners placerat felic celerati pitor eratin ac tupars.</p>
    <div class="news-meta"><span>By Reid Calloway</span><span>16 hours Ago</span></div>
  </article>
</section>

<section class="contact">
  <h2 class="section-title" style="top:2683px">CONTACT US</h2>
  <div class="section-rule" style="top:2727px"></div>
  <div class="field" style="left:193px;top:2790px;width:392px;height:52px">Name*</div>
  <div class="field" style="left:615px;top:2790px;width:395px;height:52px">Email*</div>
  <div class="field" style="left:193px;top:2869px;width:392px;height:52px">Phone</div>
  <div class="field" style="left:615px;top:2869px;width:395px;height:52px">Subject*</div>
  <div class="field" style="left:193px;top:2948px;width:817px;height:131px;padding-top:18px">Message*</div>
  <div class="btn btn-solid" style="left:193px;top:3108px;width:817px;height:52px;font-size:16px">SEND YOUR MESSAGE</div>
</section>

<footer class="site-footer">
  <div class="footer-dot"></div>
  <div class="footer-name">Tillard<br>Environmental<br>Projects</div>
  <div class="footer-heading" style="left:220px;top:190px">FOLLOW US:</div>
  <svg class="abs" style="left:174px;top:233px" width="160" height="30" aria-label="Social media links">
    <g fill="#13b092"><circle cx="12" cy="15" r="10"/><circle cx="54" cy="15" r="10"/><circle cx="96" cy="15" r="10"/><circle cx="138" cy="15" r="10"/></g>
  </svg>
  <div class="footer-heading" style="left:444px">QUICK LINKS</div>
  <ul class="footer-links" style="left:444px"><li>Products</li><li>Projects</li><li>News</li><li>Blog</li><li>Gallery</li><li>Testimonials</li></ul>
  <div class="footer-heading" style="left:647px">LOREM IMPUM</div>
  <ul class="footer-links" style="left:647px"><li>Link 1</li><li>Link 2</li><li>Link 3</li><li>Link 4</li><li>Link 5</li><li>Link 6</li></ul>
  <div class="footer-heading" style="left:874px">PHOTO GALLERY</div>
  <div class="gallery" role="img" aria-label="Gallery of environmental project photographs">
    <div style="background:linear-gradient(#dfe6de,#6e9a45)"></div>
    <div style="background:linear-gradient(#8fa070,#c9c4b8)"></div>
    <div style="background:radial-gradient(#9cd36a,#3d6b1c)"></div>
    <div style="background:radial-gradient(#e6efc4,#6a9430)"></div>
    <div style="background:linear-gradient(#dfe6de,#6e9a45)"></div>
    <div style="background:linear-gradient(#8fa070,#c9c4b8)"></div>
  </div>
  <div class="abs" style="left:136px;top:329px;width:926px;height:1px;background:#4a5048"></div>
</footer>

</body>
</html>
```